brovalux business card

We are a commercial cleaning/janitorial service company our main target is building owners and managers.
Would like to see the icon as a background shadow in the front and the full logo in white on the back with a blue background.  On the card:
Dorn Pevsky, Operations Manager, dorn@brovalux-example.com
47215-K Harlow Ave. 9 #382
Pinecrest, IN 47912
555.604.2817, 888.555.4163

Updates
please include cell 555.318.6247
                                   
Thank you
If possible the fading logo on the front should be very subtle and light and lets look at centering that as well
thanks

```html
<!DOCTYPE html>
<html lang="en">
<head>
<meta charset="utf-8">
<title>Brovalux Business Card</title>
<link rel="stylesheet" href="https://fonts.googleapis.com/css2?family=Open+Sans:wght@400;600;700&display=swap">
<style>
  :root {
    --brand-blue: #1176c2;
    --brand-blue-faint: rgba(17, 118, 194, 0.05);
    --ink-dark: #3b3b3d;
    --ink-body: #444446;
    --paper: #ffffff;
    --backdrop: #e6e6e6;
  }
  * { margin: 0; padding: 0; box-sizing: border-box; }
  html, body {
    width: 1200px; height: 960px; overflow: hidden;
    background: var(--backdrop);
    font-family: "Open Sans", Arial, sans-serif;
  }
  .canvas { position: relative; width: 1200px; height: 960px; }

  .card { position: absolute; overflow: hidden; }
  .card-back {
    left: 301px; top: 59px; width: 648px; height: 388px;
    background: var(--brand-blue);
  }
  .card-front {
    left: 294px; top: 493px; width: 666px; height: 398px;
    background: var(--paper);
  }

  .faded-mark {
    position: absolute; left: 183px; top: 49px;
    width: 300px; height: 300px; border-radius: 50%;
    background: var(--brand-blue-faint);
  }

  .brand-lockup { position: absolute; display: flex; align-items: center; }
  .brand-mark { border-radius: 50%; flex: none; }
  .brand-name { font-weight: 700; line-height: 1; letter-spacing: 0.5px; }

  .card-back .brand-lockup { left: 115px; top: 130px; gap: 18px; }
  .card-back .brand-mark { width: 106px; height: 106px; background: var(--paper); }
  .card-back .brand-name { font-size: 68px; color: var(--paper); }

  .back-website {
    position: absolute; left: 0; right: 0; top: 325px;
    text-align: center; color: var(--paper); font-size: 22px;
  }

  .card-front .brand-lockup { left: 25px; top: 160px; gap: 12px; }
  .card-front .brand-mark { width: 78px; height: 78px; background: var(--brand-blue); }
  .card-front .brand-name { font-size: 44px; color: var(--brand-blue); }

  .divider {
    position: absolute; left: 372px; top: 54px; width: 2px; height: 300px;
    background: var(--brand-blue);
  }

  .contact {
    position: absolute; left: 408px; top: 58px; width: 252px;
    color: var(--ink-body); white-space: nowrap;
  }
  .contact-name { font-size: 29px; font-weight: 700; color: var(--ink-dark); line-height: 1.2; }
  .contact-title { font-size: 14px; font-weight: 600; color: var(--brand-blue); margin-top: 2px; }
  .company { font-size: 17px; font-weight: 700; color: var(--brand-blue); margin-top: 46px; }
  .address { font-size: 15px; line-height: 21px; margin-top: 2px; }
  .lines { font-size: 15px; line-height: 20px; margin-top: 10px; letter-spacing: -0.2px; }
  .lines .label { color: var(--brand-blue); margin-right: 6px; }
  .website { color: var(--brand-blue); }
</style>
</head>
<body>
<div class="canvas">
  <section class="card card-back">
    <div class="brand-lockup">
      <span class="brand-mark"></span>
      <span class="brand-name">brovalux</span>
    </div>
    <p class="back-website">www.brovalux-example.com</p>
  </section>

  <section class="card card-front">
    <span class="faded-mark" aria-hidden="true"></span>
    <div class="brand-lockup">
      <span class="brand-mark"></span>
      <span class="brand-name">brovalux</span>
    </div>
    <div class="divider"></div>
    <div class="contact">
      <h1 class="contact-name">Dorn Pevsky</h1>
      <p class="contact-title">Operations Manager</p>
      <p class="company">Brovalux Building Services</p>
      <p class="address">47215-K Harlow Ave. 9 #382<br>Pinecrest, IN 47912</p>
      <p class="lines"><span class="label">Phone</span>888.555.4163<br><span class="label">Fax</span>555.604.2817<br><span class="label">Cell</span>555.318.6247</p>
      <p class="lines"><span class="label">E-mail</span>dorn@brovalux-example.com<br><span class="website">www.brovalux-example.com</span></p>
    </div>
  </section>
</div>
</body>
</html>
```